Executive Certificate - AI for Airports

We need a one page 8.5"x11" flyer to promote an online certificate for the implementation of AI at airports.
See attached non-professional draft for illustrative purposes only. There is no necessity to exactly emulate this draft however the attached flyer specs attached have to be adhered to.
Thank you!

Requirements
Must have
• My project must adhere to the specs provided. This includes the actual text provided in the specs document.
Should not have
• My project must not use copyrighted images.

```html
<!DOCTYPE html>
<html lang="en">
<head>
<meta charset="utf-8">
<title>Executive Certificate in Applied AI for Airports</title>
<link rel="stylesheet" href="https://fonts.googleapis.com/css2?family=Arimo:ital,wght@0,400;0,700;1,400&display=swap">
<style>
  :root{
    --white:#ffffff;
    --ink:#0b0b0b;
    --navy:#17275f;
    --brand-blue:#1b62b8;
    --brand-green:#2fae4a;
    --button-blue:#0f6cc3;
    --band-top:#0a84e6;
    --band-bottom:#08c2f6;
    --grey-band:#9b9b9b;
    --paper:#f7f8fa;
    --partner-ink:#2a2a2a;
    --hero-light:#dde6ee;
    --hero-mid:#5d87b4;
    --hero-dark:#102a57;
  }
  *{margin:0;padding:0;box-sizing:border-box}
  html,body{width:927px;height:1200px;overflow:hidden;background:var(--paper)}
  body{font-family:"Arimo",Arial,sans-serif;color:var(--ink)}
  .flyer{position:relative;width:927px;height:1200px;overflow:hidden;background:linear-gradient(180deg,#fbfbfc 0%,var(--paper) 100%)}

  .hero-photo{position:absolute;left:0;top:0;width:927px;height:597px;
    background:
      linear-gradient(180deg,rgba(26,108,208,0) 0%,rgba(26,108,208,0) 52%,rgba(24,110,210,.85) 72%,#2a7fd8 100%),
      linear-gradient(100deg,var(--hero-light) 0%,#b9c9d8 30%,var(--hero-mid) 55%,#1d3f73 75%,var(--hero-dark) 100%);}

  .org-name{position:absolute;left:33px;top:32px;display:flex;align-items:center;gap:8px;
    font-weight:700;font-size:34px;color:var(--brand-blue);letter-spacing:1px}
  .org-name .dot{width:22px;height:22px;border-radius:50%;background:var(--brand-green)}

  .headline{position:absolute;left:0;width:927px;text-align:center;color:var(--white);font-weight:700;line-height:1}
  .headline.line-1{top:270px;font-size:104px;letter-spacing:-2px;left:4px}
  .headline.line-2{top:364px;font-size:100px;left:4px}
  .program-title{position:absolute;top:461px;left:4px;width:927px;text-align:center;color:var(--white);font-size:44px;line-height:1}
  .tagline{position:absolute;top:518px;left:4px;width:927px;text-align:center;color:var(--white);font-style:italic;font-size:29px;line-height:36px}

  .feature-band{position:absolute;left:0;top:597px;width:927px;height:146px;
    background:linear-gradient(180deg,var(--band-top) 0%,var(--band-bottom) 100%);color:var(--white)}
  .feature{position:absolute;top:16px;width:380px;text-align:center;font-size:23px;line-height:27.5px}
  .feature.left{left:71px}
  .feature.right{left:477px}
  .feature-divider{position:absolute;left:459px;top:11px;width:5px;height:121px;background:var(--white)}

  .requirement-band{position:absolute;left:0;top:759px;width:927px;height:63px;background:var(--grey-band);
    color:var(--white);font-size:28.3px;line-height:63px;text-align:center}

  .format{position:absolute;top:839px;left:24px;width:927px;text-align:center;font-weight:700;font-size:37px;line-height:1}
  .session{position:absolute;top:884px;left:24px;width:927px;text-align:center;font-size:21.7px;line-height:22px}

  .register-button{position:absolute;left:393px;top:941px;width:183px;height:93px;background:var(--button-blue);
    color:var(--white);font-size:31px;line-height:30px;text-align:center;padding-top:17px;text-decoration:none}

  .website{position:absolute;top:1046px;left:22px;width:927px;text-align:center;font-style:italic;font-size:27px;color:var(--navy)}

  .partner{position:absolute;display:flex;align-items:center;gap:7px;font-weight:700}
  .partner.datavane{left:268px;top:1121px;font-size:32px;color:var(--partner-ink)}
  .partner.skyline{left:548px;top:1128px;font-size:22px;color:var(--navy)}
  .partner.skyline .dot{width:22px;height:22px;border-radius:50%;background:#3d8ad6}
</style>
</head>
<body>
<main class="flyer">
  <div class="hero-photo" role="img" aria-label="Airport apron with parked aircraft and terminal building blending into a robot working at a holographic display"></div>

  <div class="org-name"><span class="dot"></span>AERONEX</div>

  <h1>
    <span class="headline line-1">EXECUTIVE</span>
    <span class="headline line-2">CERTIFICATE</span>
  </h1>
  <p class="program-title">IN APPLIED AI FOR AIRPORTS</p>
  <p class="tagline">FAST-TRACK DATA-DRIVEN INNOVATION AND<br>DECISION-SUPPORT SYSTEMS</p>

  <section class="feature-band">
    <p class="feature left">AI Adoption at Airports<br>A Strategic Perspective a<br>Streamlined Managerial<br>Focused Program</p>
    <div class="feature-divider"></div>
    <p class="feature right">Specifically Designed for<br>Practicing Airport<br>Management Professionals<br>from All Functional Areas</p>
  </section>

  <p class="requirement-band">NO PRIOR DATA SCIENCE OR AI KNOWLEDGE REQUIRED</p>

  <p class="format">ONLINE IN REAL TIME</p>
  <p class="session">Next Session<br>November 19 to 21, 2025</p>

  <a class="register-button" href="#">REGISTER<br>NOW</a>

  <p class="website">www.skyline-institute.aero</p>

  <div class="partner datavane">Datavane</div>
  <div class="partner skyline"><span class="dot"></span>Skyline Institute</div>
</main>
</body>
</html>
```